Harborline Ted's Chinese/Dim Sum Restaurant Menu

Harborline Ted's is a seafood-asian fusion restaurant featuring dim sum and other classical asian fusion items.

We need a menu design that includes both our food menu and our drink menu.

Food menu: Needs to have space for descriptions of food (please just include a place holder and we will input them later). See attached for food menu items.

Drink menu: Just lists of items with prices. See attached Jade Pavilion Menu- please include the same items, but rebrand for Harborline Ted's.

The menus must be able to be printed in a 4.25x11in paper.

We want something modern and contemporary. My boss likes geometrical design aspects and minimalism. So, nothing too ornate. But, it has to be different from the Jade Pavilion menus. Colors can be black, red, gold or blue- but it must be able to be tied into our black and red Harborline Ted's logo. Including elements of Chinese culture, especially fishing, is a plus, but not necessary.

We also need this in ai format when we download final copy so we can edit in the future.

UPDATE: Please note, we already have a logo.

Target Market(s)

Upscale family diners

Industry/Entity Type

Chinese Food

Font styles to use
Serif
Sans Serif

Colors
0054AA
0677BA
7BADD7
CADEEF
E8F1F8
0094D4
00A9DD
6FCCEA
C7EBF8
E9F6FB
FFC000
F8CF3A
FAE287
FDF2CF
FEFAEE
EB3D1F
EC4F4E
F09395
F8D3D4
FCEDEE

Requirements
Must have
• Classic, minimalist, elegant

```html
<!DOCTYPE html>
<html lang="en">
<head>
<meta charset="utf-8">
<title>Harborline Ted's — Dim Sum Menu</title>
<link rel="stylesheet" href="https://fonts.googleapis.com/css2?family=Bellefair&family=Cormorant+Garamond:wght@500&family=Libre+Baskerville:ital@1&family=Open+Sans:wght@400&display=swap">
<style>
  :root {
    --paper: #ffffff;
    --ink: #111111;
    --gold: #b08a4e;
    --gold-soft: #c9a56a;
    --rule: #c9a56a;
  }
  * { margin: 0; padding: 0; box-sizing: border-box; }
  html, body {
    width: 1200px;
    height: 3196px;
    overflow: hidden;
    background: var(--paper);
  }
  .menu {
    position: relative;
    width: 1200px;
    height: 3196px;
    background: var(--paper);
    color: var(--ink);
  }
  .brand {
    position: absolute;
    top: 250px;
    left: 0;
    width: 1200px;
    text-align: center;
    font-family: "Bellefair", serif;
    font-size: 92px;
    line-height: 1;
    letter-spacing: 1px;
    color: var(--gold);
  }
  .section-title {
    position: absolute;
    top: 548px;
    left: 0;
    width: 1200px;
    text-align: center;
    font-family: "Cormorant Garamond", serif;
    font-weight: 500;
    font-size: 108px;
    letter-spacing: 2px;
    color: var(--gold);
    line-height: 1;
    font-variant-ligatures: none;
  }
  .dish {
    position: absolute;
    left: 0;
    width: 1200px;
    height: 320px;
  }
  .dish-photo {
    position: absolute;
    left: 4px;
    top: 0;
    width: 308px;
    height: 308px;
    border-radius: 50%;
    border: 5px solid var(--gold-soft);
    background: var(--paper);
    display: flex;
    align-items: center;
    justify-content: center;
    font-family: "Open Sans", sans-serif;
    font-size: 44px;
    color: var(--ink);
  }
  .dish-head {
    position: absolute;
    left: 326px;
    right: 0;
    top: 58px;
    height: 64px;
    border-bottom: 3px solid var(--rule);
    display: flex;
    justify-content: space-between;
    align-items: flex-end;
    padding-bottom: 14px;
  }
  .dish-name {
    font-family: "Bellefair", serif;
    font-size: 60px;
    line-height: 1;
    color: var(--gold);
  }
  .dish-price {
    font-family: "Libre Baskerville", serif;
    font-style: italic;
    font-size: 34px;
    color: var(--ink);
    padding-right: 30px;
  }
  .dish-desc {
    position: absolute;
    left: 330px;
    top: 150px;
    font-family: "Libre Baskerville", serif;
    font-style: italic;
    font-size: 34px;
    color: var(--ink);
  }
</style>
</head>
<body>
<main class="menu">
  <header class="brand">Harborline Ted's</header>

  <h1 class="section-title">DIM SUM</h1>

  <section class="dish" style="top:740px">
    <div class="dish-photo">Photo here</div>
    <div class="dish-head"><span class="dish-name">Potsticker</span><span class="dish-price">$12</span></div>
    <p class="dish-desc">Menu description here</p>
  </section>

  <section class="dish" style="top:1098px">
    <div class="dish-photo">Photo here</div>
    <div class="dish-head"><span class="dish-name">Plant-Based Dumpling</span><span class="dish-price">$11</span></div>
    <p class="dish-desc">Menu description here</p>
  </section>

  <section class="dish" style="top:1456px">
    <div class="dish-photo">Photo here</div>
    <div class="dish-head"><span class="dish-name">Lobster Dumpling</span><span class="dish-price">$13</span></div>
    <p class="dish-desc">Menu description here</p>
  </section>

  <section class="dish" style="top:1814px">
    <div class="dish-photo">Photo here</div>
    <div class="dish-head"><span class="dish-name">Sticky Rice</span><span class="dish-price">$5</span></div>
    <p class="dish-desc">Menu description here</p>
  </section>

  <section class="dish" style="top:2172px">
    <div class="dish-photo">Photo here</div>
    <div class="dish-head"><span class="dish-name">Pork Siu Mai</span><span class="dish-price">$12</span></div>
    <p class="dish-desc">Menu description here</p>
  </section>

  <section class="dish" style="top:2530px">
    <div class="dish-photo">Photo here</div>
    <div class="dish-head"><span class="dish-name">Spicy Won Ton</span><span class="dish-price">$12</span></div>
    <p class="dish-desc">Menu description here</p>
  </section>

  <section class="dish" style="top:2888px">
    <div class="dish-photo">Photo here</div>
    <div class="dish-head"><span class="dish-name">Vegan Spicy Won Ton</span><span class="dish-price">$12</span></div>
    <p class="dish-desc">Menu description here</p>
  </section>
</main>
</body>
</html>
```